Banner Project for website

We do not like our current banner and need this updated. Our website is:
https://inkvelby.com/
We need the banner to have the following wording on the left side:
See attachment. (screenshot text on the left)
On the right side, I want to replace the lady and have a nice image of printed products like the following websites which have an image with different printed prodcuts bundled together or seperately.
https://www.glavorpatch.com/
https://boxtrundo.com/
The banner must look fresh and vibrant
Target Market(s)
Small businesses
Industry/Entity Type
Printing
Requirements
Must have
- Greta banner image

```html
<!DOCTYPE html>
<html lang="en">
<head>
<meta charset="utf-8">
<title>Inkvelby – Compare Quotes and Save</title>
<link href="https://fonts.googleapis.com/css2?family=Poppins:wght@400;500;600;700&display=swap" rel="stylesheet">
<style>
  :root {
    --stage: #ababab;
    --paper: #f1f1f2;
    --paper-light: #fafafa;
    --brand-blue: #0b65a6;
    --brand-gold: #e2aa2a;
    --ink: #1e1e1e;
    --ink-soft: #2b2b2b;
    --field: #e3e3e4;
    --field-edge: #cfcfd1;
    --placeholder: #a2a2a4;
  }
  * { box-sizing: border-box; margin: 0; padding: 0; }
  html, body {
    width: 1200px; height: 1200px; overflow: hidden;
    background: var(--stage);
    font-family: "Poppins", sans-serif;
  }
  .banner {
    position: absolute; left: 63px; top: 377px;
    width: 1075px; height: 448px;
    background: linear-gradient(120deg, var(--paper-light) 0%, var(--paper) 55%, #f6f6f7 100%);
    overflow: hidden;
    box-shadow: 0 6px 14px rgba(0,0,0,0.18);
  }
  .banner__wave { position: absolute; inset: 0; width: 1075px; height: 448px; }
  .headline {
    position: absolute; left: 52px; top: 56px;
    font-size: 55px; line-height: 51px; letter-spacing: 0.5px;
    text-transform: uppercase;
  }
  .headline__lead { display: block; color: var(--brand-blue); font-weight: 600; }
  .headline__tail { display: block; color: var(--ink); font-weight: 400; }
  .headline__tail strong { font-weight: 600; }
  .intro {
    position: absolute; left: 52px; top: 173px; width: 440px;
    font-size: 18.5px; line-height: 24px; color: var(--ink-soft);
  }
  .intro + .intro { top: 229px; }
  .quote-form { position: absolute; left: 52px; top: 269px; width: 426px; }
  .quote-form__field, .quote-form__submit {
    display: flex; align-items: center;
    height: 37px; border-radius: 19px; padding-left: 22px;
    font-family: "Poppins", sans-serif; font-size: 18px;
  }
  .quote-form__field {
    background: linear-gradient(180deg, #d9d9da 0%, var(--field) 40%, #ededee 100%);
    border: 1px solid var(--field-edge);
    margin-bottom: 7px;
    box-shadow: inset 0 2px 4px rgba(0,0,0,0.12);
  }
  .quote-form__field--category { color: var(--ink); font-weight: 500; }
  .quote-form__field--sub { color: var(--placeholder); font-weight: 400; }
  .quote-form__submit {
    background: var(--brand-gold); color: var(--ink);
    border: 1px solid #c8901b; font-weight: 600; font-size: 17.5px;
    box-shadow: 0 2px 3px rgba(0,0,0,0.15);
  }
  .product-showcase {
    position: absolute; left: 595px; top: 62px;
    width: 440px; height: 340px;
    background: linear-gradient(160deg, #e7b23a 0%, #2a2a2c 35%, #1b1b1d 60%, #34465e 85%, #dcdcde 100%);
    border-radius: 4px;
    opacity: 0.9;
  }
</style>
</head>
<body>
  <section class="banner">
    <svg class="banner__wave" viewBox="0 0 1075 448" aria-hidden="true">
      <path d="M728 0 C 770 40, 800 70, 860 80 C 930 92, 940 130, 950 170 C 965 225, 1020 244, 1075 244 L1075 0 Z" fill="var(--brand-gold)"/>
      <path d="M742 0 C 780 34, 808 58, 866 70 C 942 86, 950 126, 962 164 C 976 214, 1026 236, 1075 236 L1075 0 Z" fill="var(--brand-blue)"/>
    </svg>

    <h1 class="headline">
      <span class="headline__lead">Compare Quotes</span>
      <span class="headline__tail">And <strong>Save</strong></span>
    </h1>

    <p class="intro">Get instant quotes, compare products from multiple printers and get the best price.</p>
    <p class="intro">Easy online ordering and free design.</p>

    <form class="quote-form">
      <div class="quote-form__field quote-form__field--category">What do you want to print today?</div>
      <div class="quote-form__field quote-form__field--sub">Sub Category</div>
      <div class="quote-form__submit">GET QUOTES</div>
    </form>

    <div class="product-showcase" role="img" aria-label="Bundle of printed products: branded notebook with pencil, event flyer, yellow brochure, business card, envelope and pens"></div>
  </section>
</body>
</html>
```